General Contractors need a new Crisp updated Card Design

We need a new business card design for our company of 25 years based in Toronto call Holvaster Building Inc. : Our goal is to be the leading commercial contractors in Toronto by providing exceptional value to our clients. We work very hard to deliver professional, quality, service in conjunction with consistent price competitiveness to all of our clients on every single project.

Target Market(s)

Design & Build Clients

Industry/Entity Type

Construction Company

Contact Information for Business Card

Address:
18 North Tamlin Glen Road, Unit 57, Marbrook Vale, ON, K7T 2R9
Office: 905-218-5937

Holvasters Logo
Employee Job Description
Employee Cell Phone #
Employee Email
www.holvaster-example.com

Colors

Designer to choose colors to be used in the design.

Requirements
Must have
• Quote Company Saying:
• "Professional. Quality. Service."
Nice to have
• New Crisp up to date look. simple & fresh ( Not to Busy)
Should not have
• NO BLUE PRINTS ON THE BUSINESS CARDS

```html
<!DOCTYPE html>
<html lang="en">
<head>
<meta charset="utf-8">
<title>Holvaster Building Inc. — Business Card</title>
<link rel="stylesheet" href="https://fonts.googleapis.com/css2?family=Source+Sans+3:wght@400;600;700&family=Roboto+Condensed:wght@300;400&display=swap">
<style>
  :root {
    --page: #ffffff;
    --band: #111212;
    --forest-deep: #063a33;
    --forest-mid: #0b5a4c;
    --forest-light: #17705f;
    --stripe: #00705f;
    --accent: #17a98b;
    --white: #ffffff;
    --tagline: #95aca6;
    --url-muted: #5a5d5d;
  }
  * { margin: 0; padding: 0; box-sizing: border-box; }
  html, body {
    width: 1200px; height: 1200px; overflow: hidden;
    background: var(--page);
    font-family: "Source Sans 3", "Myriad Pro", sans-serif;
  }
  .card {
    position: absolute; left: 169px; width: 840px;
    overflow: hidden;
    box-shadow: 0 18px 40px rgba(0,0,0,0.35);
  }
  .card--front { top: 84px; height: 481px; background: var(--band); }
  .card--back { top: 658px; height: 480px; background: var(--band); }

  .forest {
    position: absolute; left: 0; width: 840px;
    background:
      radial-gradient(ellipse at 50% 45%, var(--forest-mid) 0%, var(--forest-deep) 70%),
      var(--forest-deep);
  }
  .card--front .forest { top: 34px; height: 340px;
    background:
      linear-gradient(90deg, var(--forest-light) 0%, var(--forest-deep) 30%, var(--forest-deep) 70%, var(--forest-light) 100%);
  }
  .card--back .forest { top: 0; height: 430px;
    background: radial-gradient(ellipse at 60% 20%, #0d6a58 0%, var(--forest-mid) 40%, var(--forest-deep) 100%);
  }
  .stripes { position: absolute; left: 0; top: 34px; }

  .front-identity {
    position: absolute; left: 0; width: 840px; top: 194px; text-align: center; color: var(--white);
  }
  .employee-name { font-size: 38px; line-height: 40px; letter-spacing: -0.5px; font-weight: 400; }
  .employee-name strong { font-weight: 700; }
  .employee-role { font-size: 16px; line-height: 20px; margin-top: 2px; }
  .cell-icon { display: block; margin: 12px auto 0; }
  .employee-cell { font-size: 18px; margin-top: 10px; }

  .contact-row {
    position: absolute; display: flex; align-items: center; color: var(--white); font-size: 18px;
  }
  .contact-icon {
    width: 24px; height: 24px; background: var(--accent);
    display: flex; align-items: center; justify-content: center; margin-right: 18px; flex: none;
  }
  .row-address { left: 142px; top: 394px; }
  .row-phone { left: 58px; top: 432px; }
  .row-email { left: 305px; top: 432px; }
  .row-web { left: 564px; top: 432px; }
  .row-phone .contact-icon, .row-email .contact-icon, .row-web .contact-icon { margin-right: 18px; }

  .brand {
    position: absolute; left: 279px; top: 177px; display: flex; align-items: center; gap: 12px;
  }
  .brand-mark { width: 64px; height: 64px; border: 2px solid var(--white); }
  .brand-name {
    color: var(--white); font-weight: 600; font-size: 28px; line-height: 30px; letter-spacing: 1px;
  }
  .tagline {
    position: absolute; left: 0; width: 840px; top: 377px; text-align: center;
    font-family: "Roboto Condensed", "Arial Narrow", sans-serif; font-weight: 300;
    font-size: 18px; line-height: 24px; color: var(--tagline); letter-spacing: -0.3px;
  }
  .back-url {
    position: absolute; left: 0; width: 840px; top: 440px; text-align: center;
    font-weight: 700; font-size: 15px; color: var(--url-muted);
  }
</style>
</head>
<body>

<section class="card card--front">
  <div class="forest" role="img" aria-label="Photograph of a dense evergreen forest in deep teal tones"></div>
  <svg class="stripes" width="840" height="340" viewBox="0 0 840 340">
    <polygon points="247,0 331,0 147,340 63,340" fill="var(--stripe)"/>
    <polygon points="499,0 579,0 767,340 683,340" fill="var(--stripe)"/>
  </svg>

  <div class="front-identity">
    <h1 class="employee-name"><strong>EMPLOYEE</strong> NAME</h1>
    <p class="employee-role">EMPLOYEE JOB DESCRIPTION</p>
    <svg class="cell-icon" width="34" height="34" viewBox="0 0 34 34">
      <polygon points="17,0 34,17 17,34 0,17" fill="var(--accent)"/>
      <path d="M11 18 q6 -6 12 0 l-2 2 -2 -1.5 v-1.5 q-2 -1 -4 0 v1.5 l-2 1.5z" fill="#0b2a25"/>
    </svg>
    <p class="employee-cell">Employee Cell Phone</p>
  </div>

  <div class="contact-row row-address">
    <span class="contact-icon">
      <svg width="14" height="14" viewBox="0 0 14 14"><path d="M7 1 L13 7 H11 V13 H8.5 V9 H5.5 V13 H3 V7 H1z" fill="#0b2a25"/></svg>
    </span>
    18 North Tamlin Glen Road, Unit 57, Marbrook Vale, ON, K7T 2R9
  </div>
  <div class="contact-row row-phone">
    <span class="contact-icon">
      <svg width="14" height="14" viewBox="0 0 14 14"><path d="M3 1 L5.5 1 L6.5 4 L5 5.5 Q6.5 8.5 8.5 9 L10 7.5 L13 8.5 V11 Q12 13 10 13 Q2 11 1 3 Q1 1 3 1z" fill="#0b2a25"/></svg>
    </span>
    905-218-5937
  </div>
  <div class="contact-row row-email">
    <span class="contact-icon">
      <svg width="14" height="10" viewBox="0 0 14 10"><rect x="0.5" y="0.5" width="13" height="9" fill="none" stroke="#0b2a25"/><path d="M0.5 0.5 L7 6 L13.5 0.5" fill="none" stroke="#0b2a25"/></svg>
    </span>
    Employee Email
  </div>
  <div class="contact-row row-web">
    <span class="contact-icon">
      <svg width="14" height="14" viewBox="0 0 14 14" fill="none" stroke="#0b2a25" stroke-width="1"><circle cx="7" cy="7" r="6"/><ellipse cx="7" cy="7" rx="2.6" ry="6"/><path d="M1 7 H13 M2 4 H12 M2 10 H12"/></svg>
    </span>
    www.holvaster-example.com
  </div>
</section>

<section class="card card--back">
  <div class="forest" role="img" aria-label="Softly blurred photograph of an evergreen forest in teal"></div>
  <div class="brand">
    <span class="brand-mark"></span>
    <span class="brand-name">HOLVASTER<br>BUILDING INC.</span>
  </div>
  <p class="tagline">OUR GOAL IS TO BE THE LEADERS IN COMMERCIAL CONTRACTING BY DELIVERING PROFESSIONAL,<br>QUALITY, SERVICE COMBINED WITH CONSISTENT PRICE COMPETITIVENESS</p>
  <p class="back-url">www.holvaster-example.com</p>
</section>

</body>
</html>
```